Zielgruppe
Die TORVEL GMBH steht Gewerbe- und Industriekunden in verschiedensten Bereichen zur Seite. Zielsetzung unserer Ingenieur- und Energiedienstleistungen ist eine niedrigere Energiekostenbelastung, eine Subventionsmaximierung für Ihre geplanten und zukünftigen Investitionen/Projekte und die nachhaltige Nutzung regenerativer Quellen zur Eigenversorgung mit Energie und Senkung des CO2-Ausstoßes!
Aufgabenstellung
Grundlegende Überschrift über den Flyer sollte sein: Energiekosten halbieren - mit unserem 4-Säulen Programm. Diese 4 Säulen sind:
Die vier zentralen Komponenten sind:
Energieaudit gemäß DIN 16247-1 : Dieses Audit, das durch das Norlander Zentralstelle Gewerbe gefördert wird, beinhaltet eine anschließende detaillierte Inspektion der Betriebsstätte durch einen qualifizierten Ingenieur, der die Energiebräuche analysiert und einen umfassenden Bericht erstellt. Dieser zeigt auf, wie das Unternehmen auch ohne Investitionen Energie sparen kann, wobei die aktuelle durchschnittliche Einsparung bei 21 % liegt. Unsere Ingenieure sind alle KLMU-zertifiziert und arbeiten exklusiv für uns.
Beantragung von Fördergeldern : Falls das Unternehmen Investitionen plant, stehen derzeit über 8000 Förderprogramme zur Verfügung. Wir übernehmen die Prüfung und Beantragung dieses Programms für das Unternehmen. Die Fördersummen variieren, betragen im Durchschnitt jedoch 41 %.
Steueroptimierung der Energierechnung : Produzierende Unternehmen können nach Antragstellung eine Rückerstattung von 2,05 Cent pro kWh auf ihre Energierechnung erhalten. Außerdem lässt sich die Konzessionsabgabe von durchschnittlich 1,80 Cent auf 0,11 Cent senken. Diese beiden Faktoren machen in der Regel 30 % des reinen Energiepreises aus.
Verbesserung der Strom- und Gasrechnung : Durch eine Ausschreibung auf nationaler Ebene können durchschnittlich 23 % der aktuellen Energiekosten reduziert werden.

```html
<!DOCTYPE html>
<html lang="de">
<head>
<meta charset="utf-8">
<title>Energiekosten halbieren – Torvel</title>
<link rel="stylesheet" href="https://fonts.googleapis.com/css2?family=Anton&family=Poppins:wght@400;600;700;800&display=swap">
<style>
  :root {
    --stage: #bdbdbd;
    --paper: #e6e6e6;
    --ink: #1d1d1d;
    --muted: #333333;
    --green: #76c42a;
    --forest-dark: #0f2410;
    --forest-mid: #2f5a22;
    --forest-light: #6f9a4a;
    --band-dark: #161616;
    --rule: #cfcfcf;
  }
  * { box-sizing: border-box; margin: 0; padding: 0; }
  html, body { width: 1200px; height: 800px; overflow: hidden; }
  body { background: var(--stage); font-family: "Poppins", sans-serif; color: var(--ink); }

  .flyer {
    position: absolute; left: 320px; top: 8px;
    width: 560px; height: 784px;
    background: var(--paper);
    overflow: hidden;
    box-shadow: 0 6px 24px rgba(0,0,0,.25);
  }

  .hero { position: absolute; inset: 0 0 auto 0; height: 360px; }
  .hero svg { display: block; }

  .brand {
    position: absolute; top: 22px; right: 26px;
    display: flex; align-items: center; gap: 8px;
    color: #ffffff; font-weight: 600; font-size: 12px; letter-spacing: .04em;
  }
  .brand-mark { width: 14px; height: 14px; background: var(--green); }
  .brand-sub { display: block; font-size: 6.5px; font-weight: 400; letter-spacing: .14em; opacity: .85; }

  .headline {
    position: absolute; top: 150px; right: 0;
    width: 250px; padding: 18px 22px 20px;
    background: rgba(10, 20, 10, .72);
    color: #ffffff;
  }
  .headline-title {
    font-family: "Anton", sans-serif; font-size: 34px; line-height: 1.05;
    letter-spacing: .01em; text-transform: uppercase;
  }
  .headline-sub { font-family: "Anton", sans-serif; font-size: 13px; margin-top: 6px; }

  .pillars { position: absolute; top: 345px; left: 34px; right: 28px; }
  .pillar {
    display: grid; grid-template-columns: 52px 1fr; gap: 14px;
    padding: 14px 0 13px; border-bottom: 1px solid var(--rule);
  }
  .pillar:last-child { border-bottom: none; }
  .pillar-icon { width: 44px; height: 44px; margin-top: 8px; }
  .pillar-title { font-size: 12.5px; font-weight: 700; margin-bottom: 4px; }
  .pillar-text { font-size: 8.6px; line-height: 1.55; color: var(--muted); }

  .contact { position: absolute; left: 0; right: 0; bottom: 0; height: 62px; }
  .contact-dark {
    position: absolute; right: 0; top: 0; width: 100%; height: 34px;
    background: var(--band-dark);
    display: flex; justify-content: flex-end; align-items: center; gap: 14px;
    padding-right: 18px; color: #ffffff; font-size: 9px;
  }
  .contact-item { display: flex; align-items: center; gap: 5px; }
  .contact-sep { width: 1px; height: 14px; background: #777; }
  .contact-green {
    position: absolute; left: 0; bottom: 0; width: 250px; height: 62px;
    background: var(--green);
    clip-path: polygon(0 0, 86% 0, 100% 100%, 0 100%);
    color: #ffffff; font-weight: 800; font-size: 24px;
    display: flex; align-items: center; padding-left: 30px;
  }
</style>
</head>
<body>
<main class="flyer">
  <section class="hero">
    <svg width="560" height="360" viewBox="0 0 560 360">
      <defs>
        <linearGradient id="forest" x1="0" y1="0" x2="0.4" y2="1">
          <stop offset="0" stop-color="#a9b9a0"/>
          <stop offset=".35" stop-color="var(--forest-light)"/>
          <stop offset=".7" stop-color="var(--forest-mid)"/>
          <stop offset="1" stop-color="var(--forest-dark)"/>
        </linearGradient>
      </defs>
      <polygon points="0,0 560,0 560,230 0,355" fill="url(#forest)" role="img" aria-label="Foto: Glaskugel mit Weltkarte auf Moos, umgeben von Umwelt-Symbolen"/>
      <line x1="0" y1="355" x2="560" y2="230" stroke="var(--green)" stroke-width="3"/>
    </svg>
    <div class="brand">
      <span class="brand-mark"></span>
      <span>TORVEL<span class="brand-sub">TORVEL INSTITUT FÜR ENERGIE</span></span>
    </div>
    <div class="headline">
      <h1 class="headline-title">Energiekosten<br>halbieren</h1>
      <p class="headline-sub">mit unserem 4-Säulen Programm</p>
    </div>
  </section>

  <section class="pillars">
    <article class="pillar">
      <svg class="pillar-icon" viewBox="0 0 44 44" fill="none" stroke="var(--green)" stroke-width="1.6">
        <rect x="8" y="6" width="24" height="32" rx="2"/><rect x="15" y="3" width="10" height="6" rx="1"/>
        <path d="M13 17h14M13 23h14M13 29h9"/><circle cx="34" cy="32" r="6"/><path d="M31 32l2 2 4-4"/>
      </svg>
      <div>
        <h2 class="pillar-title">Energieaudit nach DIN 16247-1</h2>
        <p class="pillar-text">Bei diesem Energieaudit, das vom Norlander Zentralstelle Gewerbe zu 50% gefördert wird, führt ein zertifizierter Ingieur eine Betriebsbegehung durch und erstellt danach einen Bericht (ca. 60-70 Seiten). Darin wird genau erläutert wie das Unternehmen mit und ohne Investitionen Energie einsparen kann. Wir arbeiten ausschließlich mit eigenen, KLMU zertifizierten Ingenieuren</p>
      </div>
    </article>
    <article class="pillar">
      <svg class="pillar-icon" viewBox="0 0 44 44" fill="none" stroke="var(--green)" stroke-width="1.6">
        <rect x="11" y="4" width="22" height="36" rx="3"/><path d="M19 8h6"/>
        <circle cx="22" cy="22" r="7"/><path d="M22 18v8M20 20h3.5a1.5 1.5 0 010 3h-3a1.5 1.5 0 000 3H24"/>
      </svg>
      <div>
        <h2 class="pillar-title">Fördergelderbeantragung</h2>
        <p class="pillar-text">sofern das Unternehmen investieren möchte, gibt es aktuell über 8000 Förderprogramme. Wir prüfen und beantragen diese Förderprogramme für das Unternehmen.</p>
      </div>
    </article>
    <article class="pillar">
      <svg class="pillar-icon" viewBox="0 0 44 44" fill="none" stroke="var(--green)" stroke-width="1.6">
        <path d="M9 5h22v34l-4-3-4 3-4-3-4 3-6-3z"/><path d="M20 12v12M17 15h4.5a2 2 0 010 4h-3a2 2 0 000 4H23"/>
        <circle cx="34" cy="30" r="5"/><path d="M32 34l-1 6 3-2 3 2-1-6"/>
      </svg>
      <div>
        <h2 class="pillar-title">Steueroptimierung der Energierechnung</h2>
        <p class="pillar-text">produzierende Unternehmen erhalten nach Beantragung 2,05 cent Ihrer Energierechnung pro kwH zurück. Die Konzessionsabgabe kann bei jedem Unternehmen von durchschnittlich ca. 1,80 cent auf 0,11 cent reduziert werden. Alleine diese beiden Komponenten machen i.d.R. 50% des reinen Energiepreises aus!</p>
      </div>
    </article>
    <article class="pillar">
      <svg class="pillar-icon" viewBox="0 0 44 44" fill="none" stroke="var(--green)" stroke-width="1.6">
        <path d="M10 8h20v30H10z"/><path d="M15 16h10M15 22h10M15 28h6"/>
        <circle cx="31" cy="10" r="5"/><path d="M29 10l1.5 1.5L33 9"/><path d="M13 32l3-4-1 3h3l-3 4 1-3z"/>
      </svg>
      <div>
        <h2 class="pillar-title">Optimierung der Strom- und Gasrechnung</h2>
        <p class="pillar-text">durch eine bundesweite Ausschreibung können wir durchschnittlich 21% der aktuellen Energiekosten einsparen.</p>
      </div>
    </article>
  </section>

  <footer class="contact">
    <div class="contact-dark">
      <span class="contact-item">
        <svg width="10" height="10" viewBox="0 0 24 24" fill="#fff"><path d="M6.6 10.8a15 15 0 006.6 6.6l2.2-2.2a1 1 0 011-.25 11 11 0 003.5.56 1 1 0 011 1V20a1 1 0 01-1 1A17 17 0 013 4a1 1 0 011-1h3.5a1 1 0 011 1 11 11 0 00.56 3.5 1 1 0 01-.25 1z"/></svg>
        06100 4471290
      </span>
      <span class="contact-sep"></span>
      <span class="contact-item">
        <svg width="11" height="9" viewBox="0 0 24 18" fill="none" stroke="#fff" stroke-width="2"><rect x="1" y="1" width="22" height="16"/><path d="M1 1l11 9 11-9"/></svg>
        info@torvel.de
      </span>
      <span class="contact-sep"></span>
      <span class="contact-item">
        <svg width="10" height="10" viewBox="0 0 24 24" fill="none" stroke="#fff" stroke-width="2"><circle cx="12" cy="12" r="10"/><path d="M2 12h20M12 2c3 3 3 17 0 20M12 2c-3 3-3 17 0 20"/></svg>
        www.torvel.de
      </span>
    </div>
    <div class="contact-green">Contact Us</div>
  </footer>
</main>
</body>
</html>
```